Business Card design for an International Import Export House

We need a Business Card design for our import export business. We trade in Minerals, Metals, Rice, Sugar, Steel etc.. The design should be minimalistic. It may or may not contain the physical address. In case you want to include the physical address - 418 Marwick Plaza, Oakvale Sector 7, Halvern, Westmar, India, 560417.

Target Market(s)

Steel Mills or Steel Plants, Factories, Mining businesses, Industrial houses, Government Agencies

Industry/Entity Type

Importer

Contact Information for Business Card

Business Name - Verrano Trade

Font styles to use
Other font styles liked:
• montserrat

Requirements
Must have
• Darin Pohlak - President
• www.verranotrade.example
• darin@verranotrade.example
• +91-988-412-3675
Nice to have
• worldwide suppliers of ores

```html
<!DOCTYPE html>
<html lang="en">
<head>
<meta charset="UTF-8">
<title>Verrano Trade – Business Card</title>
<link href="https://fonts.googleapis.com/css2?family=Montserrat:wght@400;500;700&display=swap" rel="stylesheet">
<style>
  :root {
    --teal: #3f9db5;
    --teal-dark: #2f86a0;
    --ink: #1c1c1c;
    --paper: #ffffff;
    --rule: #555555;
    --backdrop: #2b2b2d;
  }
  * { margin: 0; padding: 0; box-sizing: border-box; }
  html, body {
    width: 1200px; height: 900px; overflow: hidden;
    background: var(--backdrop);
    font-family: "Montserrat", sans-serif;
  }
  .canvas { position: relative; width: 1200px; height: 900px; }

  .card {
    position: absolute;
    width: 560px; height: 320px;
    box-shadow: 0 10px 30px rgba(0,0,0,0.45);
  }

  /* Front */
  .card-front {
    left: 110px; top: 90px;
    background: linear-gradient(160deg, #49a9c0 0%, var(--teal) 55%, var(--teal-dark) 100%);
    display: flex; align-items: center; justify-content: center;
  }
  .brand {
    display: flex; align-items: center; gap: 14px;
    font-weight: 700; letter-spacing: 0.5px; text-transform: uppercase;
    white-space: nowrap;
  }
  .brand-dot { border-radius: 50%; flex: none; }
  .card-front .brand { color: var(--paper); font-size: 30px; }
  .card-front .brand-dot { width: 34px; height: 34px; border: 3px solid var(--paper); }

  /* Back */
  .card-back {
    left: 530px; top: 480px;
    background: var(--paper);
  }
  .card-back .brand {
    position: absolute; left: 40px; top: 118px;
    color: var(--teal); font-size: 21px; gap: 10px;
  }
  .card-back .brand-dot { width: 24px; height: 24px; background: var(--teal); }
  .divider {
    position: absolute; left: 0; right: 0; top: 212px;
    height: 1px; background: var(--rule);
  }
  .contact {
    position: absolute; right: 26px; top: 26px;
    text-align: right; color: var(--ink);
  }
  .person-name { font-size: 20px; font-weight: 700; letter-spacing: 0.5px; text-transform: uppercase; white-space: nowrap; }
  .person-name .first { color: var(--teal); }
  .person-role { font-size: 12px; color: var(--teal); margin-top: 1px; padding-right: 14px; }
  .name-rule { width: 200px; height: 1px; background: var(--rule); margin: 6px 14px 6px auto; }
  .line {
    font-size: 12px; line-height: 17px; font-weight: 500;
    display: flex; justify-content: flex-end; align-items: center; gap: 6px;
    white-space: nowrap;
  }
  .line .spacer, .line svg { width: 9px; height: 9px; flex: none; }
  .line svg { fill: var(--teal); }
  .web .domain { color: var(--teal); }
</style>
</head>
<body>
<div class="canvas">

  <section class="card card-front">
    <div class="brand"><span class="brand-dot"></span><span>Verrano Trade</span></div>
  </section>

  <section class="card card-back">
    <div class="brand"><span class="brand-dot"></span><span>Verrano Trade</span></div>

    <div class="contact">
      <div class="person-name"><span class="first">Darin</span> Pohlak</div>
      <div class="person-role">President</div>
      <div class="name-rule"></div>
      <div class="line"><span>418 Marwick Plaza, Oakvale Sector 7</span><span class="spacer"></span></div>
      <div class="line"><span>Halvern, Westmar, India, 560417</span><span class="spacer"></span></div>
      <div class="line"><span>+91-988-412-3675</span>
        <svg viewBox="0 0 10 10" aria-hidden="true"><path d="M2 0.5 L3.8 2.6 L2.8 3.6 Q4 6 6.4 7.2 L7.4 6.2 L9.5 8 L8.3 9.5 Q3 9 0.5 1.7 Z"/></svg>
      </div>
      <div class="line"><span>darin@verranotrade.example</span>
        <svg viewBox="0 0 10 10" aria-hidden="true"><path d="M0 2 H10 V8 H0 Z M0.8 2.6 L5 5.6 L9.2 2.6 V2.8 L5 6.3 L0.8 2.8 Z" fill-rule="evenodd"/></svg>
      </div>
      <div class="line web"><span>www.<span class="domain">verranotrade.example</span></span>
        <svg viewBox="0 0 10 10" aria-hidden="true"><circle cx="5" cy="5" r="4.5"/><path d="M0.5 5 H9.5 M5 0.5 V9.5 M5 0.5 Q2 5 5 9.5 M5 0.5 Q8 5 5 9.5" stroke="#fff" stroke-width="0.7" fill="none"/></svg>
      </div>
    </div>

    <div class="divider"></div>
  </section>

</div>
</body>
</html>
```